Welding Fabrication and Inspection Business Card Design

Welding Fabrication and Inspection Services,

Business

Industrial Machinery ServicesMohammed Rahim30 Ballarat Street, Mount Gravatt East.4122.QLD

```html
<!DOCTYPE html>
<html lang="en">
<head>
<meta charset="utf-8">
<title>Corvane Plant Services – Business Card</title>
<link href="https://fonts.googleapis.com/css2?family=Open+Sans:wght@400;600;700&display=swap" rel="stylesheet">
<style>
  :root {
    --page-bg: #ebe8e4;
    --card-top: #d8d4cf;
    --card-bottom: #c9c4be;
    --band-dark: #141414;
    --band-mid: #3a3a3a;
    --streak: #f4f4f4;
    --name-ink: #e6e6e6;
    --title-ink: #bdbdbd;
    --body-ink: #2b2b2b;
    --brand-ink: #1e1e1e;
  }
  * { margin: 0; padding: 0; box-sizing: border-box; }
  html, body {
    width: 1200px; height: 969px; overflow: hidden;
    background: var(--page-bg);
    font-family: "Open Sans", Arial, sans-serif;
  }
  .card {
    position: absolute; left: 100px; top: 200px;
    width: 1000px; height: 570px;
    background: linear-gradient(160deg, var(--card-top), var(--card-bottom));
    border: 1px solid #b8b2ab;
    box-shadow: 0 10px 30px rgba(0,0,0,0.18);
    overflow: hidden;
  }
  .card__band {
    position: absolute; left: 0; top: 0; width: 100%; height: 150px;
    background: linear-gradient(180deg, var(--band-mid) 0%, var(--band-dark) 45%, var(--band-dark) 100%);
  }
  .card__streak { position: absolute; left: 0; top: 136px; width: 100%; height: 20px; }
  .holder { position: absolute; left: 51px; top: 42px; }
  .holder__name { color: var(--name-ink); font-size: 31px; font-weight: 600; letter-spacing: 0.3px; line-height: 1.2; }
  .holder__title { color: var(--title-ink); font-size: 25px; font-weight: 400; line-height: 1.4; }
  .contact {
    position: absolute; left: 51px; top: 306px;
    color: var(--body-ink); font-size: 26px; line-height: 36px;
  }
  .contact__address { margin-bottom: 12px; }
  .contact__row { display: flex; align-items: center; gap: 10px; line-height: 38px; }
  .contact__icon { width: 24px; height: 24px; flex: none; fill: var(--body-ink); }
  .brand {
    position: absolute; right: 52px; top: 458px;
    color: var(--brand-ink); font-size: 25px; font-weight: 700;
    letter-spacing: 0.2px;
  }
</style>
</head>
<body>
  <div class="card">
    <div class="card__band"></div>
    <svg class="card__streak" viewBox="0 0 1000 20" preserveAspectRatio="none" aria-hidden="true">
      <rect x="0" y="4" width="1000" height="6" fill="var(--streak)" opacity="0.85"/>
      <rect x="0" y="10" width="1000" height="4" fill="#8d8d8d" opacity="0.6"/>
    </svg>

    <div class="holder">
      <p class="holder__name">Tariq Osmani</p>
      <p class="holder__title">President</p>
    </div>

    <div class="contact">
      <p class="contact__address">17 Windorah Street<br>Kelvin Ridge. 4127.QLD</p>
      <p class="contact__row">
        <svg class="contact__icon" viewBox="0 0 24 24" aria-hidden="true"><path d="M3 7c0-2 2-3 9-3s9 1 9 3v2h-5V7H8v2H3z"/><path d="M6 11h12l2 9H4z"/><circle cx="12" cy="15" r="2.2" fill="#d2cdc7"/></svg>
        412 508 3197
      </p>
      <p class="contact__row">
        <svg class="contact__icon" viewBox="0 0 24 24" aria-hidden="true"><path d="M2 6h20v12H2z"/><path d="M2 6l10 7 10-7" fill="none" stroke="#d2cdc7" stroke-width="1.6"/></svg>
        tariq@corvaneplant.com
      </p>
      <p class="contact__row">
        <svg class="contact__icon" viewBox="0 0 24 24" aria-hidden="true"><circle cx="12" cy="12" r="10"/><path d="M7 8c2 0 3 1 3 3s-2 2-2 4M15 5c-1 2 0 3 2 4s1 4 0 5" fill="none" stroke="#d2cdc7" stroke-width="1.6"/></svg>
        www.corvaneplant.com
      </p>
    </div>

    <p class="brand">Corvane Plant Services</p>
  </div>
</body>
</html>
```